An Iconic transformation in mattress design and comfort.

“An iconic transformation in mattress design and comfort”
We are Not Kidding here!!
This is an upstart Company, PIRZO7, LLC
Our Slogan
“dream-PIRZO”

We need an outstanding web design for an outstanding product.

It took 8 years to design this bed. It was originally designed by its owner for its owner, I continue to use it every day.

With our innovative patent pending support system, with quality throughout, simplicity in design, affordable, and proudly made here in the USA, we offer a product that is superior to anything that is in the market place now. The materials that are used deviate from the industry standard, and for good reason, our product feels incredibly plush, soft, but yet provides support that can be adjusted in a simple manor, a product that will last a lifetime.
Really, why go to work if you can lay in this bed all day; you'll want to work from home! A quick nap, you'll be in heaven.

Overall Web design:
We like the web site “taltrunex.com”, sleek, modern, a site that seems to add credibility to their product by issuing registration numbers for their tops, not a bad idea for our beds. Its important to understand that this industry is filled with smoke and mirrors, over pricing, very poor quality, and show rooms filled with sales people that are piranhas.; we seek to distance ourselves! This company will sell its product not in the traditional show room but online. Please also see these websites: www.brimvora.com, www.nudlet.com

Last thing I want to see is a another website filled with beds, what to do? Well perhaps a few shots of our beds is ok, after all thats what we are selling. An idea here; I was listening to a news show, this man decided to tell his story with tattoos on his own body! Interesting, different approach (not that I'm into tattoos); website design with innovation through simplicity and creative thinking and marketing.

The photos of our product have yet to be taken by a professional. We have yet to find a way to photograph this product in a different and innovative manner.

Target Market(s)

Millennials

Industry/Entity Type

It Company

Number of Pages Required

4 page

Font styles to use
Serif

Colors
ec1f27

Requirements
Must have
• Existing logo
Nice to have
• See project description
• Can further expand upon, upon request for specifics.
Should not have
• See project description

```html
<!DOCTYPE html>
<html lang="en">
<head>
<meta charset="utf-8">
<title>PIRZO7 — An Iconic Transformation in Mattress Design &amp; Comfort</title>
<link href="https://fonts.googleapis.com/css2?family=Bebas+Neue&family=Questrial&family=Open+Sans:wght@400;600;700&display=swap" rel="stylesheet">
<style>
:root{
  --red:#ec1f27;
  --red-dark:#b3141b;
  --ink:#222222;
  --text:#555555;
  --muted:#8a8a8a;
  --paper:#ffffff;
  --soft:#f5f5f5;
  --line:#e2e2e2;
  --linen:#f4f3f0;
  --skin:#e3c7b0;
  --skin-deep:#c49a7c;
  --wood:#8a5f3e;
}
*{margin:0;padding:0;box-sizing:border-box}
html,body{width:1200px;height:3429px;overflow:hidden}
body{position:relative;background:var(--paper);font-family:"Open Sans",Arial,sans-serif;color:var(--text)}
.abs{position:absolute}
.heading{font-family:"Questrial",Arial,sans-serif;color:var(--ink);font-weight:400;letter-spacing:1px}
.heading em{font-style:normal;color:var(--red)}
.btn{position:absolute;display:flex;align-items:center;justify-content:center;font-family:"Open Sans",sans-serif;font-weight:700;font-size:14px;letter-spacing:.5px;color:#fff;background:var(--red);text-transform:uppercase;text-decoration:none}
.brand{font-family:"Questrial",Arial,sans-serif;color:var(--ink);font-size:40px;line-height:1}

/* header */
.site-header{left:0;top:0;width:1200px;height:94px;background:#fff;border-top:5px solid var(--red)}
.site-header .brand{position:absolute;left:80px;top:16px}
.site-header .tagline{position:absolute;left:100px;top:60px;font-size:12px;color:var(--muted);font-family:"Questrial",sans-serif}
.nav{position:absolute;top:21px;left:295px;display:flex}
.nav a{display:block;height:44px;line-height:44px;padding:0 18px;margin-right:16px;font-family:"Open Sans",sans-serif;font-size:15px;color:var(--ink);text-decoration:none}
.nav a.active{background:var(--red);color:#fff;outline:2px solid #333;outline-offset:-4px}
.cart{position:absolute;left:1060px;top:21px;width:62px;height:44px;background:var(--red);display:flex;align-items:center;justify-content:center;gap:8px;color:#fff;font-size:15px}

/* hero */
.hero-photo{left:0;top:94px;width:1200px;height:583px;
  background:
    radial-gradient(ellipse 260px 220px at 470px 150px,rgba(227,199,176,.75),rgba(227,199,176,0) 70%),
    radial-gradient(ellipse 520px 300px at 260px 520px,#ffffff 0%,rgba(255,255,255,0) 75%),
    radial-gradient(ellipse 380px 260px at 140px 140px,#ffffff 0%,rgba(255,255,255,0) 80%),
    radial-gradient(ellipse 160px 300px at 560px 200px,rgba(120,150,90,.35),rgba(120,150,90,0) 70%),
    linear-gradient(180deg,rgba(0,0,0,0) 55%,rgba(200,200,196,.45) 80%,rgba(235,235,232,.6) 100%),
    linear-gradient(90deg,#ecebe7 0%,#e2e1dc 35%,#d9d8d2 55%,#e9e8e3 75%,#f3f2ef 100%)}
.hero-title{left:752px;top:220px;font-family:"Bebas Neue",sans-serif;font-size:84px;color:var(--red);letter-spacing:2px;line-height:1}
.hero-sub{left:752px;top:304px;font-family:"Questrial",sans-serif;font-size:38px;line-height:52px;color:#2b2b2b}
.btn-outline{background:#fff;color:var(--red);border:2px solid var(--red)}

/* welcome */
.welcome-title{left:0;width:1200px;top:726px;text-align:center;font-size:42px}
.welcome-text{left:136px;width:928px;top:786px;text-align:center;font-size:13px;line-height:23px}

/* why */
.why{left:0;top:999px;width:1200px;height:521px;background:var(--soft)}
.why-title{left:0;width:1200px;top:50px;text-align:center;font-size:42px}
.feature{position:absolute;font-family:"Questrial",sans-serif;font-size:21px;color:#333;line-height:24px}
.mattress{left:247px;top:199px;width:706px;height:133px;border-radius:6px;box-shadow:0 10px 18px rgba(0,0,0,.18);
  background:linear-gradient(180deg,#ffffff 0%,#f3f3f3 40%,#dadada 46%,#1f1f1f 48%,#1f1f1f 50%,#4b4b4b 52%,#3a3a3a 100%)}

/* gallery */
.tile{position:absolute;width:300px;height:209px}
.caption{left:300px;top:149px;width:300px;height:61px;background:rgba(236,31,39,.9);color:#fff;padding:8px 22px}
.caption strong{display:block;font-family:"Questrial",sans-serif;font-weight:400;font-size:20px;line-height:24px}
.caption span{font-size:13px}

/* cleanable */
.clean-title{left:80px;top:1984px;font-size:40px;line-height:50px}
.clean-text{left:80px;top:2100px;width:500px;font-size:14px;line-height:24px}
.video{left:631px;top:1989px;width:490px;height:290px;background:#fff;border:1px solid var(--line);box-shadow:0 0 8px rgba(0,0,0,.12);padding:12px}
.video-frame{width:100%;height:100%;
  background:
    radial-gradient(ellipse 200px 60px at 230px 160px,#f2ede4,rgba(242,237,228,0) 80%),
    linear-gradient(180deg,#5d4b38 0%,#7d6a55 35%,#e6e1d8 50%,#d8d2c6 62%,#3f3f3f 66%,#4a4a4a 78%,#6b5440 80%,#5a4330 100%)}
.video-bar{position:absolute;left:12px;right:12px;bottom:12px;height:26px;background:#1b1b1b}

/* testimonials */
.testi{left:0;top:2332px;width:1200px;height:400px;
  background:
    radial-gradient(ellipse 260px 240px at 180px 230px,rgba(227,199,176,.55),rgba(227,199,176,0) 75%),
    radial-gradient(ellipse 240px 240px at 1040px 160px,rgba(214,184,160,.6),rgba(214,184,160,0) 75%),
    linear-gradient(90deg,#efe6df 0%,#f8f4f1 45%,#f6f1ee 65%,#e9ded6 100%)}
.testi-title{left:0;width:1200px;top:42px;text-align:center;font-size:42px}
.quote{left:288px;top:105px;width:624px;height:208px;background:rgba(236,31,39,.78);color:#fff;padding:20px 32px}
.quote p{font-size:13.5px;line-height:23px;margin-top:10px}
.stars{text-align:center;color:#ffd54a;font-size:18px;letter-spacing:2px}
.who{position:absolute;right:80px;bottom:26px;text-align:right;font-family:"Questrial",sans-serif}
.who b{font-weight:400;font-size:18px;display:block}
.who i{font-size:13px}
.avatar{position:absolute;right:28px;bottom:24px;width:46px;height:46px;border-radius:50%;background:radial-gradient(circle at 50% 40%,#e6cdb8,#b48f74);border:2px solid #fff}
.dots{left:560px;top:2676px;display:flex;gap:26px;align-items:center}
.dot{width:6px;height:6px;border-radius:50%;background:var(--red)}
.dot.on{width:14px;height:14px;box-shadow:0 0 0 4px #fff}

/* faq */
.faq-photo{left:549px;top:2732px;width:651px;height:407px;
  background:
    radial-gradient(ellipse 200px 170px at 420px 160px,rgba(224,190,160,.9),rgba(224,190,160,0) 75%),
    radial-gradient(ellipse 240px 200px at 430px 60px,rgba(236,214,160,.85),rgba(236,214,160,0) 75%),
    linear-gradient(180deg,rgba(0,0,0,0) 70%,rgba(225,220,212,.9) 100%),
    linear-gradient(90deg,#ffffff 0%,#ffffff 18%,#efe6dc 38%,#dfcdba 65%,#d7c6b4 100%)}
.faq-title{left:80px;top:2778px;font-size:40px}
.faq-list{left:80px;top:2843px;width:640px;list-style:none}
.faq-list li{font-size:14.5px;color:var(--red);line-height:36px}
.faq-list li.open{line-height:24px}
.faq-list li .answer{display:block;color:var(--text);font-size:13.5px;line-height:23px;padding-left:24px;margin-bottom:14px}
.faq-list .sign{display:inline-block;width:16px;color:#888}

/* footer */
.footer{left:0;top:3139px;width:1200px;height:240px;background:var(--red);color:#fff}
.footer h4{position:absolute;top:30px;font-family:"Open Sans",sans-serif;font-weight:600;font-size:16px;letter-spacing:.5px}
.f-item{position:absolute;font-size:13.5px;line-height:20px;display:flex;gap:14px;align-items:flex-start}
.news-thumb{width:52px;height:52px;border-radius:50%;background:radial-gradient(circle at 50% 40%,#ead3c0,#b8917a);border:2px solid #fff;flex:none}
.news-date{font-size:11.5px;opacity:.9}
.email{position:absolute;left:608px;top:123px;width:248px;height:40px;border:1px solid rgba(255,255,255,.7);display:flex;align-items:center;gap:12px;padding-left:10px;font-style:italic;font-size:13px}
.subscribe{position:absolute;left:730px;top:173px;width:126px;height:40px;background:#2a2a2a;color:#fff;font-size:14px;display:flex;align-items:center;justify-content:center}
.footer .brand{position:absolute;left:922px;top:58px;color:#fff;font-size:44px}
.footer .tagline{position:absolute;left:950px;top:104px;font-size:12px;font-family:"Questrial",sans-serif}
.social{position:absolute;left:938px;top:130px;display:flex;gap:12px}
.social span{width:34px;height:34px;border-radius:50%;background:#fff}
.copyright{left:0;top:3379px;width:1200px;height:50px;background:var(--red-dark);color:#fff;text-align:center;line-height:50px;font-size:13px}
.copyright b{font-weight:400;color:#ff8a8f}
</style>
</head>
<body>

<header class="abs site-header">
  <div class="brand">PIRZO7</div>
  <div class="tagline">dream-PIRZO</div>
  <nav class="nav">
    <a class="active" href="#">HOME</a>
    <a href="#">ABOUT</a>
    <a href="#">QUALITY</a>
    <a href="#">STORE</a>
    <a href="#">GALLERY</a>
    <a href="#">NEWS</a>
    <a href="#">CONTACT</a>
  </nav>
  <div class="cart">
    <svg width="22" height="20" viewBox="0 0 22 20" fill="none" stroke="#fff" stroke-width="2"><path d="M1 2h4l3 11h10l3-8H7"/><circle cx="9" cy="17" r="1.6" fill="#fff"/><circle cx="17" cy="17" r="1.6" fill="#fff"/></svg>
    <span>0</span>
  </div>
</header>

<section>
  <div class="abs hero-photo" role="img" aria-label="Woman stretching happily after waking in a white bed in a bright bedroom"></div>
  <h1 class="abs hero-title">AN ICONIC</h1>
  <p class="abs hero-sub">Transformation in<br>Mattress Design &amp;<br>Comfort</p>
  <a class="btn btn-outline" style="left:750px;top:491px;width:137px;height:51px">ENTER SHOP</a>
  <a class="btn" style="left:896px;top:491px;width:135px;height:51px">PLAY VIDEO</a>
</section>

<section>
  <h2 class="abs heading welcome-title">WELCOME TO <em>PIRZO7</em></h2>
  <p class="abs welcome-text">With our innovative patent pending support system, with quality throughout, simplicity in design, affordable, and proudly made here in the USA, we offer a product that is superior to anything that is in the market place now. The materials that are used deviate from the industry standard, and for good reason, our product feels incredibly plush, soft, but yet provides support that can be adjusted in a simple manor, a product that will last a lifetime.</p>
  <a class="btn" style="left:533px;top:896px;width:134px;height:50px">READ MORE</a>
</section>

<section class="abs why">
  <h2 class="abs heading why-title">WHY <em>PIRZO7?</em></h2>
  <svg class="abs" style="left:0;top:0" width="1200" height="521" viewBox="0 0 1200 521" fill="none" stroke="#f08a8e" stroke-width="1.5" stroke-dasharray="3 4">
    <path d="M300 130H445V190"/><path d="M900 130H750V190"/>
    <path d="M445 332V392H300"/><path d="M750 332V392H900"/>
    <path d="M600 332V415"/>
    <g stroke-dasharray="none" fill="#fff" stroke="#ec1f27">
      <circle cx="300" cy="130" r="4"/><circle cx="445" cy="130" r="4"/><circle cx="900" cy="130" r="4"/><circle cx="750" cy="130" r="4"/>
      <circle cx="300" cy="392" r="4"/><circle cx="445" cy="392" r="4"/><circle cx="900" cy="392" r="4"/><circle cx="750" cy="392" r="4"/>
      <circle cx="600" cy="415" r="4"/>
    </g>
  </svg>
  <span class="feature" style="left:88px;top:116px">Simplicity in Design</span>
  <span class="feature" style="left:913px;top:116px">Product feels<br>Incredibly Plush</span>
  <span class="feature" style="left:456px;top:172px">Industry Standard Materials</span>
  <div class="abs mattress" role="img" aria-label="Product shot of the mattress: white quilted top over a dark grey knit base"></div>
  <span class="feature" style="left:175px;top:380px">Affordable</span>
  <span class="feature" style="left:913px;top:380px">Made in USA</span>
  <span class="feature" style="left:506px;top:438px">Lifetime Warranty</span>
</section>

<section class="abs" style="left:0;top:1520px;width:1200px;height:418px">
  <div class="tile" style="left:0;top:0;background:radial-gradient(ellipse 120px 70px at 120px 90px,#e8c7ad,rgba(232,199,173,0) 80%),linear-gradient(180deg,#d9cfc6 0%,#efebe6 55%,#ffffff 100%)" role="img" aria-label="Woman sleeping peacefully on a white pillow"></div>
  <div class="tile" style="left:300px;top:0;background:radial-gradient(ellipse 150px 60px at 150px 150px,#ffffff,rgba(255,255,255,0) 80%),linear-gradient(180deg,#c9b8a6 0%,#e6ddd3 45%,#f4f1ed 100%)" role="img" aria-label="Neatly made bed with cushions in a warm bedroom"></div>
  <div class="tile" style="left:600px;top:0;background:radial-gradient(ellipse 110px 60px at 140px 80px,#e6cbb6,rgba(230,203,182,0) 80%),linear-gradient(180deg,#f3f1ee 0%,#e5e2de 60%,#ffffff 100%)" role="img" aria-label="Children playing under white bedsheets"></div>
  <div class="tile" style="left:900px;top:0;background:radial-gradient(ellipse 140px 80px at 130px 100px,#dcb79b,rgba(220,183,155,0) 80%),linear-gradient(180deg,#f0e8df 0%,#e3d6c8 50%,#ffffff 100%)" role="img" aria-label="Man relaxing in bed with a cup of coffee"></div>
  <div class="tile" style="left:0;top:209px;background:radial-gradient(ellipse 150px 70px at 140px 100px,#c79d80,rgba(199,157,128,0) 80%),linear-gradient(180deg,#e9e4df 0%,#f6f4f1 60%,#ffffff 100%)" role="img" aria-label="Couple sleeping together in white bedding"></div>
  <div class="tile" style="left:300px;top:209px;background:radial-gradient(ellipse 130px 70px at 160px 110px,#e2c1a6,rgba(226,193,166,0) 80%),linear-gradient(180deg,#e6ddd5 0%,#f6f3f0 55%,#ffffff 100%)" role="img" aria-label="Mother and daughter resting on a bed"></div>
  <div class="tile" style="left:600px;top:209px;background:radial-gradient(ellipse 90px 110px at 150px 100px,#b88c6e,rgba(184,140,110,0) 80%),linear-gradient(180deg,#d8cfc6 0%,#ece7e2 60%,#f8f7f5 100%)" role="img" aria-label="Woman in striped top drinking tea in bed"></div>
  <div class="tile" style="left:900px;top:209px;background:linear-gradient(180deg,#e4e7e9 0%,#d3d5d6 35%,#4b4c4e 52%,#5b5c5e 62%,#a67650 66%,#8a5f3e 100%)" role="img" aria-label="Woman tying her running shoes on the edge of a mattress"></div>
  <div class="abs caption"><strong>Lorem Ipsum is simply</strong><span>Lorem Ipsum is simply dummy text of</span></div>
</section>

<section>
  <h2 class="abs heading clean-title">COMPLETLY CLEANABLE<br>100% FRESH</h2>
  <p class="abs clean-text">Lorem Ipsum is simply dummy text of the printing and typesetting industry. Lorem Ipsum has been the industry's standard dummy text ever since the 1500s, when an unknown printer took a galley of type and scrambled it to make a type specimen book.</p>
  <a class="btn" style="left:78px;top:2229px;width:134px;height:50px">READ MORE</a>
  <div class="abs video">
    <div class="video-frame" role="img" aria-label="Video still of the mattress on a wooden floor"></div>
    <div class="video-bar">
      <svg width="466" height="26" viewBox="0 0 466 26"><rect x="0" y="0" width="466" height="3" fill="#555"/><rect x="0" y="0" width="40" height="3" fill="#ec1f27"/><circle cx="40" cy="2" r="4" fill="#ec1f27"/><path d="M10 9l8 5-8 5z" fill="#ddd"/><rect x="430" y="9" width="12" height="9" fill="none" stroke="#ddd"/></svg>
    </div>
  </div>
</section>

<section class="abs testi" role="img" aria-label="Soft faded background of a smiling father and daughter">
  <h2 class="abs heading testi-title">WHAT CUSTOMERS SAY</h2>
  <div class="abs quote">
    <div class="stars">★★★★★</div>
    <p>"Lorem Ipsum is simply dummy text of the printing and typesetting industry. Lorem Ipsum has been the industry's standard dummy text ever since the 1500s, when an unknown printer took a galley of type and scrambled it to make a type specimen book.</p>
    <div class="who"><b>Marin Tolve</b><i>London</i></div>
    <div class="avatar" role="img" aria-label="Customer portrait"></div>
  </div>
</section>
<div class="abs dots"><span class="dot"></span><span class="dot on"></span><span class="dot"></span></div>

<section>
  <div class="abs faq-photo" role="img" aria-label="Smiling blonde woman lying on a soft white rug"></div>
  <h2 class="abs heading faq-title">FAQ</h2>
  <ul class="abs faq-list">
    <li class="open"><span class="sign">–</span>Lorem Ipsum is simply dummy text of the printing and typesetting industry?
      <span class="answer">Lorem Ipsum is simply dummy text of the printing and typesetting industry.<br>Lorem Ipsum has been the industry's standard dummy text ever since the<br>1500s, when an unknown printer took a galley of type and scrambled it.</span></li>
    <li><span class="sign">+</span>Lorem Ipsum is simply dummy text of the printing</li>
    <li><span class="sign">+</span>Lorem Ipsum is simply dummy text of the printing</li>
    <li><span class="sign">+</span>Lorem Ipsum is simply dummy text of the printing</li>
    <li><span class="sign">+</span>Lorem Ipsum is simply dummy text of the printing</li>
  </ul>
</section>

<footer class="abs footer">
  <h4 style="left:80px">CONTACT INFO</h4>
  <div class="f-item" style="left:80px;top:66px">
    <svg width="20" height="20" viewBox="0 0 20 20" fill="none" stroke="#fff" stroke-width="1.6"><path d="M2 4l5-2 6 2 5-2v14l-5 2-6-2-5 2z"/><path d="M7 2v14M13 4v14"/></svg>
    <span>123 Building Name, Stret, Area,<br>Citry, Country - Zipcode</span></div>
  <div class="f-item" style="left:80px;top:128px">
    <svg width="20" height="20" viewBox="0 0 20 20" fill="none" stroke="#fff" stroke-width="1.6"><path d="M4 2h4l2 5-3 2a11 11 0 0 0 4 4l2-3 5 2v4a2 2 0 0 1-2 2A16 16 0 0 1 2 4a2 2 0 0 1 2-2z"/></svg>
    <span>123 4567 890</span></div>
  <div class="f-item" style="left:80px;top:174px">
    <svg width="20" height="20" viewBox="0 0 20 20" fill="none" stroke="#fff" stroke-width="1.6"><rect x="2" y="4" width="16" height="12"/><path d="M2 4l8 7 8-7"/></svg>
    <span>help@pirzo7.com</span></div>

  <h4 style="left:345px">NEWS</h4>
  <div class="f-item" style="left:345px;top:68px"><span class="news-thumb" role="img" aria-label="News thumbnail"></span><span>Lorem Ipsum is simply<br>dummy text of the printing<br><span class="news-date">Today 5:60 pm - 12.06.2016</span></span></div>
  <div class="f-item" style="left:345px;top:140px"><span class="news-thumb" role="img" aria-label="News thumbnail"></span><span>Lorem Ipsum is simply<br>dummy text of the printing<br><span class="news-date">Today 2:10 pm - 12.06.2016</span></span></div>

  <h4 style="left:608px">NEWSLETTER</h4>
  <p class="abs" style="left:608px;top:68px;width:260px;font-size:13.5px;line-height:22px">Subscribe to get news &amp; Updates of our work</p>
  <div class="email">
    <svg width="18" height="14" viewBox="0 0 18 14" fill="none" stroke="#fff" stroke-width="1.5"><rect x="1" y="1" width="16" height="12"/><path d="M1 1l8 7 8-7"/></svg>
    <span>Enter E-Mail Id</span></div>
  <div class="subscribe">SUBSCRIBE</div>

  <div class="brand">PIRZO7</div>
  <div class="tagline">dream-PIRZO</div>
  <div class="social"><span></span><span></span><span></span></div>
</footer>
<div class="abs copyright">© <b>PIRZO7</b> - 2016. All Rights Reserved.</div>

</body>
</html>
```